Enterprise image desing

The designs are for a fashion store for young men and women.
Updates

Los diseƱos parecen similares

Target Market(s)

Young

Font styles to use
Sans Serif

Colors
ec1f27
ffffff
1b1b1b

Requirements
Must have
• Use clean and modern sources
Nice to have
• n / a
Should not have
• n / a

```html
<!DOCTYPE html>
<html lang="en">
<head>
<meta charset="utf-8">
<title>Veltrano Stationery Set</title>
<link href="https://fonts.googleapis.com/css2?family=Montserrat:wght@800&family=Arimo:wght@400;700&family=Lato:wght@400&family=Dancing+Script:wght@500&display=swap" rel="stylesheet">
<style>
  :root {
    --red: #d5262f;
    --red-soft: #dc3d3b;
    --ink: #1b1b1b;
    --white: #ffffff;
    --blush: #fcefea;
    --mist: #e4e4e8;
    --backdrop: #2b2b2b;
  }
  html, body { margin: 0; padding: 0; overflow: hidden; background: var(--backdrop); }
  .board { display: block; width: 1189px; height: 1200px; }
  .brand { font-family: "Montserrat", sans-serif; font-weight: 800; letter-spacing: 0.5px; }
  .brand--ink { fill: var(--ink); }
  .brand--white { fill: var(--white); }
  .contact { font-family: "Lato", sans-serif; font-size: 8.5px; fill: var(--ink); }
  .web { font-family: "Lato", sans-serif; font-size: 8.5px; letter-spacing: 1px; fill: var(--ink); }
  .web--white { fill: var(--white); }
  .web--tiny { font-size: 4px; letter-spacing: 0.3px; }
  .letter { font-family: "Arimo", sans-serif; font-size: 9.2px; fill: var(--ink); }
  .letter-name { font-size: 10px; }
  .letter-strong { font-family: "Arimo", sans-serif; font-weight: 700; font-size: 10px; fill: var(--ink); }
  .signature { font-family: "Dancing Script", cursive; font-size: 34px; fill: var(--ink); }
  .fill-red { fill: var(--red); }
  .fill-white { fill: var(--white); }
  .fill-ink { fill: var(--ink); }
  .deco-warm { fill: url(#warm-wash); }
  .deco-light { fill: url(#light-wash); }
</style>
</head>
<body>
<svg class="board" viewBox="0 0 1457 1470" xmlns="http://www.w3.org/2000/svg">
  <defs>
    <linearGradient id="warm-wash" x1="0" y1="0" x2="1" y2="1">
      <stop offset="0" stop-color="#d5262f"/>
      <stop offset="1" stop-color="#df4441"/>
    </linearGradient>
    <linearGradient id="light-wash" x1="0" y1="0" x2="1" y2="1">
      <stop offset="0" stop-color="#ffffff"/>
      <stop offset="0.55" stop-color="#fcefea"/>
      <stop offset="1" stop-color="#e6e6ea"/>
    </linearGradient>
    <pattern id="spiral-rings" x="0" y="1052" width="24" height="13" patternUnits="userSpaceOnUse">
      <rect x="0" y="2" width="24" height="5" rx="2.5" fill="#cfcfcf"/>
    </pattern>
  </defs>

  <!-- Presentation folder -->
  <g class="folder">
    <rect x="147" y="87" width="550" height="710" class="fill-red"/>
    <rect x="167" y="87" width="3" height="710" fill="#b81f27"/>
    <g role="img" aria-label="Decorative brand graphic area">
      <rect x="230" y="316" width="467" height="481" class="deco-warm"/>
    </g>
    <rect x="297" y="168" width="34" height="34" class="fill-white"/>
    <text x="345" y="199" class="brand brand--white" font-size="34">VELTRANO</text>
    <text x="374" y="752" class="web web--white">www.veltrano.com</text>
  </g>

  <!-- Letterhead -->
  <g class="letterhead">
    <rect x="785" y="89" width="502" height="708" class="fill-white"/>
    <g role="img" aria-label="Decorative brand graphic area">
      <rect x="843" y="305" width="444" height="450" class="deco-light"/>
    </g>
    <rect x="819" y="141" width="26" height="26" class="fill-red"/>
    <text x="854" y="163" class="brand brand--ink" font-size="26">VELTRANO</text>
    <rect x="1122" y="132" width="1.2" height="42" class="fill-ink"/>
    <text class="contact">
      <tspan x="1136" y="139">Calle Olmos y Ribera,</tspan>
      <tspan x="1136" y="149">Loja - Ecuador, EC110101</tspan>
      <tspan x="1148" y="163">+593 7 200 1100</tspan>
      <tspan x="1148" y="173">info@veltrano.com</tspan>
    </text>
    <rect x="1138" y="157" width="4" height="6" class="fill-red"/>
    <rect x="1138" y="167" width="5" height="4" class="fill-red"/>

    <text x="819" y="309" class="letter-strong">JOHN SMITH</text>
    <text class="letter"><tspan x="819" y="325">Street Name,City Name.</tspan><tspan x="819" y="335">Zip Coad 0000</tspan></text>
    <text class="letter">
      <tspan x="819" y="382">Lorem Ipsum is simply dummy text of the printing and typesetting industry. Lorem Ipsum has been the</tspan>
      <tspan x="819" y="397">industry's standard dummy text ever since the 1500s, when an unknown printer took a galley of type and</tspan>
      <tspan x="819" y="412">scrambled it to make a type specimen book. It has survived not only five centuries,but also the leap into</tspan>
      <tspan x="819" y="427">electronic typesetting, remaining essentially unchanged. It was popularised in the 1960s with the release</tspan>
      <tspan x="819" y="442">of sample sheets containing Lorem Ipsum passages, and more recently with desktop publishing software</tspan>
      <tspan x="819" y="457">like common layout programs including versions of Lorem Ipsum.</tspan>
      <tspan x="819" y="488">It is a long established fact that a reader will be distracted by the readable content of a page when looking</tspan>
      <tspan x="819" y="503">at its layout. The point of using Lorem Ipsum is that it has a more-or-less normal distribution of letters, as</tspan>
      <tspan x="819" y="518">opposed to using 'Content here, content here', making it look like readable English. Many desktop and</tspan>
      <tspan x="819" y="533">years, sometimes by accident, sometimes on purpose (injected humour and the like).</tspan>
      <tspan x="819" y="581">Regards,</tspan>
    </text>
    <text x="819" y="624" class="signature">John Doe</text>
    <text class="letter"><tspan x="819" y="646" class="letter-name">John Doe</tspan><tspan x="819" y="657">General Maneger</tspan></text>

    <rect x="785" y="770" width="355" height="1" class="fill-red"/>
    <rect x="1250" y="770" width="37" height="1" class="fill-red"/>
    <text x="1150" y="772" class="web">www.veltrano.com</text>
    <rect x="785" y="777" width="502" height="10" class="fill-red"/>
  </g>

  <!-- Envelope front -->
  <g class="envelope-front">
    <rect x="147" y="847" width="495" height="248" class="fill-white"/>
    <g role="img" aria-label="Decorative brand graphic area">
      <rect x="440" y="848" width="202" height="214" class="deco-light"/>
    </g>
    <rect x="173" y="884" width="24" height="24" class="fill-red"/>
    <text x="206" y="905" class="brand brand--ink" font-size="24">VELTRANO</text>
    <rect x="173" y="1018" width="1.2" height="38" class="fill-ink"/>
    <text class="contact">
      <tspan x="186" y="1024">Calle Olmos y Ribera,</tspan>
      <tspan x="186" y="1034">Loja - Ecuador, EC110101</tspan>
      <tspan x="197" y="1047">+593 7 200 1100</tspan>
      <tspan x="197" y="1056">info@veltrano.com</tspan>
    </text>
    <rect x="188" y="1041" width="4" height="6" class="fill-red"/>
    <rect x="188" y="1050" width="5" height="4" class="fill-red"/>
    <rect x="147" y="1072" width="357" height="1" class="fill-red"/>
    <text x="510" y="1074" class="web">www.veltrano.com</text>
    <rect x="147" y="1080" width="495" height="8" class="fill-red"/>
  </g>

  <!-- Envelope back -->
  <g class="envelope-back">
    <rect x="147" y="1135" width="495" height="248" class="fill-white"/>
    <path d="M147,1135 H642 L634,1200 Q632,1212 620,1212 H165 Q153,1212 152,1200 Z" class="fill-red"/>
    <rect x="342" y="1166" width="15" height="15" class="fill-white"/>
    <text x="362" y="1180" class="brand brand--white" font-size="16">VELTRANO</text>
  </g>

  <!-- Erasers -->
  <g class="eraser-white">
    <rect x="935" y="862" width="130" height="60" class="fill-white"/>
    <rect x="1065" y="862" width="28" height="60" fill="#3a3a3a"/>
    <rect x="965" y="889" width="9" height="9" class="fill-red"/>
    <text x="978" y="898" class="brand brand--ink" font-size="11">VELTRANO</text>
  </g>
  <g class="eraser-red">
    <rect x="1137" y="862" width="131" height="60" class="fill-red"/>
    <rect x="1268" y="862" width="29" height="60" fill="#ededed"/>
    <rect x="1169" y="889" width="9" height="9" class="fill-white"/>
    <text x="1182" y="898" class="brand brand--white" font-size="11">VELTRANO</text>
  </g>

  <!-- Business card front -->
  <g class="card-front">
    <rect x="692" y="970" width="333" height="190" class="fill-white"/>
    <g role="img" aria-label="Decorative brand graphic area">
      <rect x="872" y="970" width="153" height="158" class="deco-light"/>
    </g>
    <rect x="708" y="999" width="21" height="21" class="fill-red"/>
    <text x="736" y="1017" class="brand brand--ink" font-size="21">VELTRANO</text>
    <text class="contact">
      <tspan x="708" y="1064">Calle Olmos y Ribera</tspan>
      <tspan x="708" y="1074">Loja - Ecuador, EC110101</tspan>
      <tspan x="721" y="1101">+593 98 100 2200</tspan>
      <tspan x="721" y="1111">+593 7 200 1100</tspan>
      <tspan x="721" y="1121">mrivas@veltrano.com</tspan>
    </text>
    <rect x="710" y="1094" width="4" height="7" class="fill-red"/>
    <rect x="710" y="1105" width="4" height="6" class="fill-red"/>
    <rect x="709" y="1115" width="5" height="4" class="fill-red"/>
    <rect x="692" y="1138" width="206" height="1" class="fill-red"/>
    <rect x="998" y="1138" width="27" height="1" class="fill-red"/>
    <text x="904" y="1140" class="web">www.veltrano.com</text>
    <rect x="692" y="1145" width="333" height="7" class="fill-red"/>
  </g>

  <!-- Business card back -->
  <g class="card-back">
    <rect x="694" y="1195" width="329" height="188" class="fill-red"/>
    <g role="img" aria-label="Decorative brand graphic area">
      <rect x="848" y="1210" width="175" height="173" class="deco-warm"/>
    </g>
    <rect x="773" y="1278" width="23" height="23" class="fill-white"/>
    <text x="805" y="1298" class="brand brand--white" font-size="24">VELTRANO</text>
  </g>

  <!-- Spiral notebook -->
  <g class="notebook">
    <rect x="1065" y="1042" width="245" height="341" class="fill-red"/>
    <g role="img" aria-label="Decorative brand graphic area">
      <rect x="1100" y="1152" width="210" height="231" class="deco-warm"/>
    </g>
    <rect x="1058" y="1052" width="24" height="318" fill="url(#spiral-rings)"/>
    <rect x="1132" y="1081" width="16" height="16" class="fill-white"/>
    <text x="1153" y="1096" class="brand brand--white" font-size="17">VELTRANO</text>
    <text x="1166" y="1361" class="web web--white web--tiny">www.veltrano.com</text>
  </g>
</svg>
</body>
</html>
```